Quorlapex

Hi everyone!

Looks like our project is more sophisticated than we expected. So good news - we increased the budget! and one of you will sure get the prize - no money back for us!

We are a young Russian company that specializes in in-taxi entertainment. We believe that our key strength is great attention to user experience. We've devoted much effort to improve ergonomics of our devices - tablet PCs that we install in the taxis. And yes, we enjoy to simplify things!

Now we need the most basic things - a logo and some staff for client meetings (primarily advertisers and ad agencies).

As for logo - we already have one engraved on the prototypes of our device (see attached file). This is one of the ideas (still far from perfect) - what we appreciate in it is minimalistic yet stylish approach.

As for "take it to the meeting stuff" we want to start with name card, pen and notepad (A4) that we will leave in clients's office, also as a reminder. Shall your have more smart ideas - always welcome!

As for logo and name cards - we would like to make an image of serious but modern company. Our design should communicate creativity and reliability. We believe that "to understand is to simplify" - minimalistic design is the most difficult one. Its better to work hard on fonts and arrangement, than put 10 variegated images.

SO THE TASK IS TO DESIGN:
- a logo
- a name card
- a note pad (great example in attachment)
- a pen

Shall you have more questions - please ask in comments.

We look forward to meeting like-minded fellows here!

Target Market(s)

Out target are:

- advertiser
- advertising agencies
- taxi passenger

Industry/Entity Type

It Company

Requirements
Must have
• font should be chosen very carefully
Nice to have
• classic minimalistic plain text only but very stylish name card is a dream of one of our co-founders:)
Should not have
• we do not want to have taxi-like colors and chess-boards. We are closer to "innovation", "entertainment", and "user experience", rather than "taxi".

```html
<!DOCTYPE html>
<html lang="en">
<head>
<meta charset="utf-8">
<title>Quorlapex — A4 Notepad</title>
<link href="https://fonts.googleapis.com/css2?family=Quicksand:wght@300&family=Noto+Serif:wght@400&display=swap" rel="stylesheet">
<style>
  :root {
    --canvas: #ffffff;
    --paper: #ffffff;
    --brand-blue: #4a6f8a;
    --ink-navy: #1f3d5a;
    --divider-grey: #b9c3cc;
  }
  html, body {
    margin: 0;
    padding: 0;
    width: 1200px;
    height: 1000px;
    overflow: hidden;
    background: var(--canvas);
  }
  .notepad-sheet {
    position: absolute;
    left: 280px;
    top: 48px;
    width: 639px;
    height: 903px;
    background: var(--paper);
    box-shadow: 0 0 12px rgba(0, 0, 0, 0.28);
  }
  .brand-wordmark {
    position: absolute;
    top: 22px;
    left: 0;
    width: 100%;
    text-align: center;
    font-family: "Quicksand", sans-serif;
    font-weight: 300;
    font-size: 50px;
    letter-spacing: 0.5px;
    color: var(--brand-blue);
    line-height: 1;
    margin: 0;
  }
  .page-arrow {
    position: absolute;
    top: 435px;
    width: 22px;
    height: 34px;
  }
  .page-arrow--prev { left: 28px; }
  .page-arrow--next { right: 28px; }
  .contact-line {
    position: absolute;
    bottom: 27px;
    left: 0;
    width: 100%;
    display: flex;
    justify-content: center;
    align-items: center;
    gap: 7px;
    font-family: "Noto Serif", serif;
    font-size: 8px;
    color: var(--ink-navy);
  }
  .contact-line .separator {
    color: var(--divider-grey);
    font-size: 7px;
  }
</style>
</head>
<body>
  <main class="notepad-sheet">
    <h1 class="brand-wordmark">quorlapex</h1>

    <svg class="page-arrow page-arrow--prev" viewBox="0 0 22 34" aria-hidden="true">
      <polyline points="18,3 4,17 18,31" fill="none" stroke="var(--brand-blue)" stroke-width="3.2" stroke-linecap="round" stroke-linejoin="round"/>
    </svg>
    <svg class="page-arrow page-arrow--next" viewBox="0 0 22 34" aria-hidden="true">
      <polyline points="4,3 18,17 4,31" fill="none" stroke="var(--brand-blue)" stroke-width="3.2" stroke-linecap="round" stroke-linejoin="round"/>
    </svg>

    <footer class="contact-line">
      <span class="separator">‹</span>
      <span class="contact-phone">+7 55501284</span>
      <span class="separator">›</span>
      <span class="contact-email">hello@quorlapex.com</span>
      <span class="separator">›</span>
      <span class="contact-web">www.quorlapex.com</span>
      <span class="separator">›</span>
    </footer>
  </main>
</body>
</html>
```